Delicious BBQ Sauce package design!

We need a corner-pouch doypack (see attached) design that aligns with our logo (which is a cartoon and intended to depict a fun and delicious bbq sauce) and can accommodate three variants of the sauce (maybe just changing the name of the sauce and adding a slight visual differentiator?). The design needs to include the following:
1. "Spicin' it up since '96!" as banner
2. Logo
3. Name of sauce (as the differentiator. There are three): Harbor Blend, Cinder Blend, Summit Blend
4. "Zesty and Tangy BBQ Sauce"
5. Actual image of bbq sauce (close up, not in container) as background to entire package. Samples attached. Let me know if you have a better idea!
6. UPC code (different for each sauce variant)
7. Company URL: www.dorvanmeats.com
8. Splash for "First Place Sauce Winner at MTDL event!" with small image of the trophy. Attached.
9. Nutrition panel and ingredients
10. QR Code

Also open to your suggestions to make this packaging great!

Target Market(s)

People who love bbq sauce

Industry/Entity Type

Retail

Font styles to use
Sans Serif

Colors

Designer to choose colors to be used in the design.

Requirements
Must have
• The design needs to include the following:
• 1. "Spicin' it up since '96!" as banner
• 2. Logo
• 3. Name of sauce (as the differentiator. There are three): Harbor Blend, Cinder Blend, Summit Blend
• 4. "Zesty and Tangy BBQ Sauce"
• 5. Actual image of bbq sauce (close up, not in container) as background to entire package. Samples attached. Let me know if you have a better idea!
• 6. UPC code (different for each sauce variant)
• 7. Company URL: www.dorvanmeats.com
• 8. Splash for "First Place Sauce Winner at MTDL event!" with small image of the trophy. Attached.
• 9. Nutrition panel and ingredients
• 10. QR Code
Nice to have
• Open to suggestions that will make packaging appealing and will get people to buy it.

```html
<!DOCTYPE html>
<html lang="en">
<head>
<meta charset="utf-8">
<title>Dorvan Meats – Harbor Blend BBQ Sauce Pouch</title>
<link rel="stylesheet" href="https://fonts.googleapis.com/css2?family=Yellowtail&family=Cinzel:wght@700&family=Bungee&family=Open+Sans:wght@600;700&family=Oswald:wght@600&display=swap">
<style>
  :root {
    --stage: #2b2b2b;
    --sauce-light: #c9581c;
    --sauce-mid: #b24410;
    --sauce-dark: #8e2f0a;
    --gold: #f2d21b;
    --ink: #111111;
    --stripe-red: #9c1f0e;
    --badge-med: #f0a020;
    --badge-low: #7cc242;
    --badge-high: #e8262a;
    --panel-white: #ffffff;
    --band-yellow: #f5e61e;
    --logo-tone: #7a1d0a;
  }
  html, body {
    margin: 0;
    width: 1200px;
    height: 848px;
    overflow: hidden;
    background: var(--stage);
  }
  .pouch-front {
    position: absolute;
    left: 360px;
    top: 62px;
    width: 480px;
    height: 724px;
  }
  .tagline-arc { font-family: "Yellowtail", cursive; font-size: 40px; fill: var(--gold); stroke: var(--ink); stroke-width: 1.2px; paint-order: stroke; }
  .brand-name { font-family: "Cinzel", serif; font-weight: 700; font-size: 36px; fill: var(--gold); }
  .variant-name { font-family: "Cinzel", serif; font-weight: 700; font-size: 34px; fill: var(--gold); }
  .descriptor { font-family: "Bungee", sans-serif; font-size: 21px; fill: var(--gold); stroke: var(--ink); stroke-width: 1px; paint-order: stroke; }
  .award-text { font-family: "Open Sans", sans-serif; font-weight: 700; font-size: 7.4px; fill: var(--ink); letter-spacing: 0.3px; }
  .gda-level { font-family: "Open Sans", sans-serif; font-weight: 700; font-size: 13px; }
  .gda-label { font-family: "Open Sans", sans-serif; font-weight: 600; font-size: 10px; fill: var(--ink); }
  .gda-value { font-family: "Open Sans", sans-serif; font-weight: 600; font-size: 14px; fill: var(--ink); }
  .gda-percent { font-family: "Open Sans", sans-serif; font-weight: 700; font-size: 17px; fill: var(--ink); }
  .net-weight { font-family: "Oswald", sans-serif; font-weight: 600; font-size: 18px; fill: var(--ink); letter-spacing: 1.5px; }
</style>
</head>
<body>
<svg class="pouch-front" viewBox="0 0 480 724" xmlns="http://www.w3.org/2000/svg">
  <defs>
    <linearGradient id="sauce-gradient" x1="0" y1="0" x2="1" y2="1">
      <stop offset="0" stop-color="var(--sauce-light)"/>
      <stop offset="0.55" stop-color="var(--sauce-mid)"/>
      <stop offset="1" stop-color="var(--sauce-dark)"/>
    </linearGradient>
    <radialGradient id="trophy-tone" cx="0.5" cy="0.4" r="0.6">
      <stop offset="0" stop-color="#f7e08a"/>
      <stop offset="1" stop-color="#b8892a"/>
    </radialGradient>
    <clipPath id="pouch-shape">
      <path d="M112 0 H480 V724 H0 V158 Z"/>
    </clipPath>
    <path id="tagline-path" d="M76 330 A164 164 0 0 1 404 330"/>
    <path id="award-ring" d="M365 146 A36 36 0 1 1 365.1 146"/>
    <path id="variant-path" d="M80 482 Q240 510 400 464"/>
  </defs>

  <g clip-path="url(#pouch-shape)">
    <rect class="sauce-background" x="0" y="0" width="480" height="724" fill="url(#sauce-gradient)" role="img" aria-label="Close-up photograph of glossy BBQ sauce with spice flecks"/>

    <g class="award-splash">
      <circle cx="365" cy="110" r="56" fill="var(--gold)"/>
      <circle cx="310" cy="72" r="7" fill="var(--gold)"/>
      <circle cx="424" cy="60" r="6" fill="var(--gold)"/>
      <circle cx="430" cy="160" r="8" fill="var(--gold)"/>
      <circle cx="300" cy="150" r="5" fill="var(--gold)"/>
      <circle cx="365" cy="110" r="30" fill="var(--ink)"/>
      <circle cx="365" cy="110" r="16" fill="url(#trophy-tone)" role="img" aria-label="Small gold trophy illustration"/>
      <text class="award-text"><textPath href="#award-ring" startOffset="2%">FIRST PLACE SAUCE WINNER AT MTDL EVENT!</textPath></text>
    </g>

    <text class="tagline-arc"><textPath href="#tagline-path" startOffset="50%" text-anchor="middle">Spicin' it up since '96!</textPath></text>

    <g class="brand-mark">
      <circle cx="240" cy="300" r="90" fill="var(--logo-tone)" role="img" aria-label="Brand illustration area"/>
      <text class="brand-name" x="240" y="410" text-anchor="middle">Dorvan Meats</text>
    </g>

    <g class="side-stripes" stroke="var(--ink)" stroke-width="2">
      <rect x="0" y="446" width="80" height="50" fill="var(--stripe-red)" stroke="none"/>
      <rect x="400" y="446" width="80" height="50" fill="var(--stripe-red)" stroke="none"/>
      <line x1="0" y1="448" x2="80" y2="448"/><line x1="0" y1="456" x2="80" y2="456"/>
      <line x1="0" y1="464" x2="80" y2="464"/><line x1="0" y1="472" x2="80" y2="472"/>
      <line x1="0" y1="480" x2="80" y2="480"/><line x1="0" y1="488" x2="80" y2="488"/>
      <line x1="0" y1="495" x2="80" y2="495"/>
      <line x1="400" y1="448" x2="480" y2="448"/><line x1="400" y1="456" x2="480" y2="456"/>
      <line x1="400" y1="464" x2="480" y2="464"/><line x1="400" y1="472" x2="480" y2="472"/>
      <line x1="400" y1="480" x2="480" y2="480"/><line x1="400" y1="488" x2="480" y2="488"/>
      <line x1="400" y1="495" x2="480" y2="495"/>
    </g>

    <path class="variant-ribbon" d="M66 436 Q240 460 414 420 L414 480 Q240 520 66 496 Z" fill="var(--ink)"/>
    <text class="variant-name"><textPath href="#variant-path" startOffset="50%" text-anchor="middle">HARBOR BLEND</textPath></text>

    <text class="descriptor" x="243" y="556" text-anchor="middle" textLength="360" lengthAdjust="spacingAndGlyphs">ZESTY AND TANGY BBQ SAUCE</text>

    <g class="nutrition-guide">
      <g class="gda gda-med" transform="translate(148 575)">
        <rect width="52" height="98" rx="20" fill="var(--badge-med)"/>
        <rect x="4" y="20" width="44" height="46" fill="var(--panel-white)"/>
        <text class="gda-level" x="26" y="15" text-anchor="middle" fill="var(--ink)">MED</text>
        <text class="gda-label" x="26" y="33" text-anchor="middle">Calories</text>
        <text class="gda-value" x="26" y="55" text-anchor="middle">353</text>
        <text class="gda-percent" x="26" y="87" text-anchor="middle">18%</text>
      </g>
      <g class="gda gda-low" transform="translate(207 575)">
        <rect width="52" height="98" rx="20" fill="var(--badge-low)"/>
        <rect x="4" y="20" width="44" height="46" fill="var(--panel-white)"/>
        <text class="gda-level" x="26" y="15" text-anchor="middle" fill="var(--panel-white)">LOW</text>
        <text class="gda-label" x="26" y="33" text-anchor="middle">Sugar</text>
        <text class="gda-value" x="26" y="55" text-anchor="middle">0.9g</text>
        <text class="gda-percent" x="26" y="87" text-anchor="middle">1%</text>
      </g>
      <g class="gda gda-high" transform="translate(264 575)">
        <rect width="52" height="98" rx="20" fill="var(--badge-high)"/>
        <rect x="4" y="20" width="44" height="46" fill="var(--panel-white)"/>
        <text class="gda-level" x="26" y="15" text-anchor="middle" fill="var(--panel-white)">HIGH</text>
        <text class="gda-label" x="26" y="33" text-anchor="middle">Sat Fat</text>
        <text class="gda-value" x="26" y="55" text-anchor="middle">10.8g</text>
        <text class="gda-percent" x="26" y="87" text-anchor="middle">54%</text>
      </g>
    </g>

    <rect class="weight-band" x="0" y="680" width="480" height="44" fill="var(--band-yellow)"/>
    <text class="net-weight" x="240" y="709" text-anchor="middle">NET WEIGHT</text>
  </g>
</svg>
</body>
</html>
```